Photography Business Card Design

I want a simple,classy design using a logo and simple font such as minion pro or similar. I have attached a logo that I quite like or am open to something similar. On the back of the card I would like the attached photo possibly with my website address on it some where. I want a matt black with silver or grey print. Possibly have the logo off to one side with the words Daniel Festerby Photography stacked on top of each other
Updates
I am very sorry that some how I forgot to put my facebook address on the details section, www.socialpage.example/DanielFesterbyPhotography
If this could be include on the card as well.
Industry/Entity Type
Business
Contact Information for Business Card
Daniel Festerby Photography
www.danielfesterbyphotography.example.au
Email: danielfesterby@wirenest.example
Phone: +61 (0)427 318 502
Logo Text
Logo styles of interest
Abstract Logo
Look and feel

```html
<!DOCTYPE html>
<html lang="en">
<head>
<meta charset="utf-8">
<title>Daniel Festerby Photography – Business Card</title>
<link rel="stylesheet" href="https://fonts.googleapis.com/css2?family=Tenor+Sans&display=swap">
<style>
  :root {
    --backdrop: #2a2a2a;
    --card-black: #1f1f1f;
    --accent-cyan: #2bb8dc;
    --print-grey: #d2d2d2;
    --photo-light: #bdbdbd;
    --photo-mid: #6e6e6e;
    --photo-dark: #151515;
  }
  html, body {
    margin: 0;
    width: 1200px;
    height: 900px;
    overflow: hidden;
    background: var(--backdrop);
    font-family: "Tenor Sans", sans-serif;
  }
  .canvas {
    position: relative;
    width: 1200px;
    height: 900px;
  }
  .card {
    position: absolute;
    width: 520px;
    height: 318px;
    box-shadow: 0 14px 30px rgba(0,0,0,0.55);
    overflow: hidden;
  }
  /* Back of card */
  .card-back {
    left: 150px;
    top: 110px;
  }
  .card-back .photo {
    position: absolute;
    inset: 0;
    background:
      linear-gradient(to bottom, rgba(21,21,21,0) 55%, var(--photo-dark) 100%),
      radial-gradient(ellipse at 55% 45%, var(--photo-light) 0%, var(--photo-mid) 45%, var(--photo-dark) 85%);
  }
  .card-back .website {
    position: absolute;
    right: 16px;
    bottom: 14px;
    color: #f2f2f2;
    font-size: 11px;
    letter-spacing: 0.3px;
  }
  /* Front of card */
  .card-front {
    left: 530px;
    top: 470px;
    background: var(--card-black);
  }
  .brand {
    position: absolute;
    left: 30px;
    top: 46px;
    display: flex;
    align-items: center;
    gap: 14px;
  }
  .brand-mark {
    width: 46px;
    height: 46px;
    border-radius: 50%;
    background: var(--accent-cyan);
  }
  .brand-name {
    color: var(--accent-cyan);
    font-size: 22px;
    line-height: 1.05;
  }
  .contact {
    position: absolute;
    right: 18px;
    top: 126px;
    text-align: right;
    color: var(--print-grey);
    font-size: 13.5px;
  }
  .contact .person {
    color: var(--accent-cyan);
    font-size: 22px;
    margin: 0 24px 4px 0;
  }
  .contact ul {
    list-style: none;
    margin: 0;
    padding: 0;
  }
  .contact li {
    display: flex;
    justify-content: flex-end;
    align-items: center;
    gap: 6px;
    height: 21px;
  }
  .contact li.no-icon { padding-right: 20px; }
  .icon {
    width: 14px;
    height: 14px;
    flex: none;
  }
</style>
</head>
<body>
<main class="canvas">

  <section class="card card-back">
    <div class="photo" role="img" aria-label="Black and white photograph of tall pine trees silhouetted against a bright cloudy sky"></div>
    <span class="website">www.danielfesterbyphotography.example.au</span>
  </section>

  <section class="card card-front">
    <div class="brand">
      <span class="brand-mark"></span>
      <span class="brand-name">Daniel Festerby<br>Photography</span>
    </div>

    <div class="contact">
      <div class="person">Daniel Festerby</div>
      <ul>
        <li>+61 (0)427 318 502
          <svg class="icon" viewBox="0 0 14 14"><circle cx="7" cy="7" r="6.2" fill="none" stroke="var(--accent-cyan)" stroke-width="1.2"/><path d="M5 4.2 l1.2 1.6 -0.7 0.8 q0.8 1.5 2 2.1 l0.8 -0.7 1.6 1.2 -0.8 1 q-3.6 -0.6 -5 -5 z" fill="var(--accent-cyan)"/></svg>
        </li>
        <li>danielfesterby@wirenest.example
          <svg class="icon" viewBox="0 0 14 14"><circle cx="7" cy="7" r="6.2" fill="none" stroke="var(--accent-cyan)" stroke-width="1.2"/><rect x="4" y="5" width="6" height="4.2" fill="none" stroke="var(--accent-cyan)" stroke-width="0.9"/><path d="M4 5 l3 2.3 3 -2.3" fill="none" stroke="var(--accent-cyan)" stroke-width="0.9"/></svg>
        </li>
        <li>www.danielfesterbyphotography.example.au
          <svg class="icon" viewBox="0 0 14 14"><circle cx="7" cy="7" r="6.2" fill="none" stroke="var(--accent-cyan)" stroke-width="1.2"/><circle cx="7" cy="7" r="3" fill="none" stroke="var(--accent-cyan)" stroke-width="0.9"/><path d="M4 7 h6" stroke="var(--accent-cyan)" stroke-width="0.9"/></svg>
        </li>
        <li>www.socialpage.example/DanielFesterbyPhotography
          <svg class="icon" viewBox="0 0 14 14"><circle cx="7" cy="7" r="6.2" fill="none" stroke="var(--accent-cyan)" stroke-width="1.2"/></svg>
        </li>
      </ul>
    </div>
  </section>

</main>
</body>
</html>
```